Audio-Visual & Video Communications Business Requires a Cutting-edge Business Card Design

LinkHarbor is a new Audio-Visual & Video Communications company in Cape Town, South Africa that is looking for a cutting-edge business card design. We sell these products to the Corporate, Education & Hospitality markets and will also host an Online Shop for companies and individuals to purchase our products online.

We are already using the following two colours in our logo and draft website. Please incorporate these colours into the design. Please note that our website is still in the design stage if you need to visit it. Green #a0ce4e & Dark Grey #333333.
Updates

Hi,

Please note that I have uploaded our logo in an .eps format.

Target Market(s)

Corporate Companies, Education Institutions & Hospitality Markets

Industry/Entity Type

Business

Requirements
Nice to have
• It would be great if you could incorporate the services that we offer.

1. Consultation & Design
2. Project Management
3. Supply & Installation
4. Onsite Support Personal
5. Online Shop

```html
<!DOCTYPE html>
<html lang="en">
<head>
<meta charset="utf-8">
<title>LinkHarbor Business Card</title>
<link rel="stylesheet" href="https://fonts.googleapis.com/css2?family=Open+Sans:wght@300;400;600;700&display=swap">
<style>
  :root {
    --green: #a0ce4e;
    --green-deep: #4ea754;
    --green-shade: #3f9446;
    --grey-dark: #333333;
    --grey-mid: #6d6d6d;
    --grey-soft: #f1f1ef;
    --white: #ffffff;
    --backdrop: #d9d9d9;
  }
  * { margin: 0; padding: 0; box-sizing: border-box; }
  html, body { width: 1200px; height: 900px; overflow: hidden; }
  body {
    background: var(--backdrop);
    font-family: "Open Sans", Arial, sans-serif;
    display: flex;
    flex-direction: column;
    align-items: center;
    justify-content: center;
    gap: 40px;
  }
  .card {
    width: 700px;
    height: 400px;
    position: relative;
    overflow: hidden;
    box-shadow: 0 4px 14px rgba(0,0,0,0.18);
  }

  /* Front */
  .card-front { background: var(--white); }
  .front-ring {
    position: absolute;
    right: 40px; top: 70px;
    width: 250px; height: 250px;
    border-radius: 50%;
    background: var(--grey-soft);
  }
  .contact { position: absolute; left: 46px; top: 38px; color: var(--grey-mid); }
  .contact-name {
    font-weight: 300;
    font-size: 40px;
    color: var(--green);
    letter-spacing: 0.5px;
    line-height: 1;
  }
  .contact-address { font-size: 11px; font-weight: 300; margin: 10px 0 0 4px; line-height: 1.4; }
  .contact-list { list-style: none; margin: 20px 0 0 4px; }
  .contact-list li {
    display: flex; align-items: center; gap: 12px;
    font-size: 15px; font-weight: 300; line-height: 28px;
  }
  .contact-list svg { width: 14px; height: 14px; fill: var(--green-deep); flex: none; }
  .front-brand {
    position: absolute; right: 50px; top: 205px;
    display: flex; align-items: center; gap: 12px;
    font-size: 44px; font-weight: 700; color: var(--grey-dark);
  }
  .brand-dot { width: 26px; height: 26px; border-radius: 50%; background: var(--green); }

  .services {
    position: absolute; left: 0; right: 0; bottom: 0;
  }
  .services-list {
    list-style: none;
    display: flex; justify-content: space-between;
    padding: 0 26px 7px;
    font-size: 11px; color: var(--green-deep);
  }
  .services-bar { display: flex; height: 14px; }
  .services-bar .bar-grey { width: 34%; background: var(--grey-dark); opacity: 0.18; }
  .services-bar .bar-green { flex: 1; background: var(--green-deep); }

  /* Back */
  .card-back { background: var(--green-deep); }
  .back-ring {
    position: absolute; left: -110px; top: -20px;
    width: 340px; height: 340px; border-radius: 50%;
    background: var(--green-shade);
  }
  .back-brand {
    position: absolute; right: 60px; top: 50%; transform: translateY(-50%);
    display: flex; align-items: center; gap: 14px;
    font-size: 46px; font-weight: 700; color: var(--white);
  }
  .back-brand .brand-dot { background: var(--white); width: 28px; height: 28px; }
</style>
</head>
<body>
  <section class="card card-front" aria-label="Business card front">
    <div class="front-ring"></div>
    <div class="contact">
      <h1 class="contact-name">Sam Rowe</h1>
      <p class="contact-address">PO Box 2140, Observatory, Cape Town,<br>7925, South Africa</p>
      <ul class="contact-list">
        <li>
          <svg viewBox="0 0 24 24"><path d="M6.6 10.8a15.1 15.1 0 0 0 6.6 6.6l2.2-2.2c.3-.3.7-.4 1-.2 1.1.4 2.3.6 3.6.6.6 0 1 .4 1 1V20c0 .6-.4 1-1 1A17 17 0 0 1 3 4c0-.6.4-1 1-1h3.5c.6 0 1 .4 1 1 0 1.3.2 2.5.6 3.6.1.3 0 .7-.2 1z"/></svg>
          xxx xxx xxxx
        </li>
        <li>
          <svg viewBox="0 0 24 24"><path d="M2 5h20v14H2zm2 2v.5l8 5 8-5V7l-8 5z"/></svg>
          enquiries@linkharbor.com
        </li>
        <li>
          <svg viewBox="0 0 24 24"><path d="M12 2a10 10 0 1 0 0 20 10 10 0 0 0 0-20zm6.9 6h-3a15 15 0 0 0-1.3-3.9A8 8 0 0 1 18.9 8zM12 4c.8 1.2 1.5 2.5 1.9 4h-3.8c.4-1.5 1.1-2.8 1.9-4zM4.3 14a8 8 0 0 1 0-4h3.4a16 16 0 0 0 0 4zm.8 2h3a15 15 0 0 0 1.3 3.9A8 8 0 0 1 5.1 16zm3-8h-3a8 8 0 0 1 4.3-3.9A15 15 0 0 0 8.1 8zM12 20c-.8-1.2-1.5-2.5-1.9-4h3.8c-.4 1.5-1.1 2.8-1.9 4zm2.3-6H9.7a14 14 0 0 1 0-4h4.6a14 14 0 0 1 0 4zm.3 5.9a15 15 0 0 0 1.3-3.9h3a8 8 0 0 1-4.3 3.9zm1.7-5.9a16 16 0 0 0 0-4h3.4a8 8 0 0 1 0 4z"/></svg>
          linkharbor.com
        </li>
      </ul>
    </div>
    <div class="front-brand"><span class="brand-dot"></span>LinkHarbor</div>
    <div class="services">
      <ul class="services-list">
        <li>Consultation &amp; Design</li>
        <li>Project Management</li>
        <li>Supply &amp; Installation</li>
        <li>Onsite Support Personal</li>
        <li>Online Shop</li>
      </ul>
      <div class="services-bar"><span class="bar-grey"></span><span class="bar-green"></span></div>
    </div>
  </section>

  <section class="card card-back" aria-label="Business card back">
    <div class="back-ring"></div>
    <div class="back-brand"><span class="brand-dot"></span>LinkHarbor</div>
  </section>
</body>
</html>
```